Power point presentation optimization, in terms of content design

I have a completed business presentation, with all the texting, but I need some design improvement in terms of text formatting, lettering, text boxes, arrows, bullets, shapes and their formatting, relative location of text boxes and pictures in the slide, etc, etc, so that this specific presentation becomes more visually appealing.
Our company power point template is available.
I´m providing our company power point template (to be used as a reference) as well as the presentation that needs to be improved.

Target Market(s)

Potential partner in business.

Industry/Entity Type

Health

Requirements
Nice to have
• More ellegant collors (more according to the template) on the picture of slide 7. A more elegant dollar image (slide 16).

```html
<!DOCTYPE html>
<html lang="pt">
<head>
<meta charset="utf-8">
<title>Clínica Horizonte – Apresentação</title>
<link href="https://fonts.googleapis.com/css2?family=Montserrat:wght@300;400;600;700;800&display=swap" rel="stylesheet">
<style>
:root{
  --navy:#0d6c9f;
  --blue:#1a8fc4;
  --sky:#3aa8da;
  --pale:#e9f3f8;
  --ink:#3d4a55;
  --grey:#7c868e;
  --mute:#b9c2c8;
  --page:#ffffff;
}
*{box-sizing:border-box;margin:0;padding:0}
html,body{width:1200px;height:1200px;overflow:hidden;background:var(--page);font-family:'Montserrat',sans-serif;color:var(--ink)}
.deck{position:relative;width:1200px;height:1200px;padding:78px 0 0 56px;display:grid;grid-template-columns:repeat(3,336px);grid-auto-rows:189px;column-gap:43px;row-gap:26.25px}
.slide{position:relative;background:#fff;overflow:hidden;box-shadow:0 4px 12px rgba(0,0,0,.18)}
.abs{position:absolute}
.ph{position:absolute}
.footer{position:absolute;left:0;right:0;bottom:0;height:9px;background:linear-gradient(115deg,var(--navy) 0 68%,#fff 68% 68.7%,var(--blue) 68.7%);font-size:3.4px;color:#fff;display:flex;justify-content:space-between;align-items:center;padding:0 14px}
.slide-title{position:absolute;left:9px;top:8px;border-left:2px solid var(--sky);padding-left:4px;font-size:8.5px;color:var(--blue);font-weight:400;line-height:10px}
.slide-title b{font-weight:700}
.brand{position:absolute;display:flex;align-items:center;gap:3px;color:var(--blue);font-weight:800;white-space:nowrap}
.brand i{display:block;border-radius:50%;background:var(--blue)}
.brand.small{right:8px;top:9px;font-size:5px}
.brand.small i{width:7px;height:7px}
.bullets{list-style:none}
.bullets li{position:relative;padding-left:8px}
.bullets li::before{content:"";position:absolute;left:0;top:.35em;width:3px;height:3px;border:1px solid var(--blue);border-radius:50%}
.bio-head{font-size:4.6px;font-weight:700;color:var(--navy);margin:6px 0 2.5px}
.bio-head:first-child{margin-top:0}
.photo-doctor{background:linear-gradient(135deg,#d6e4ec,#9fb6c3 60%,#5d7788)}
.photo-dark{background:linear-gradient(160deg,#3a3f44,#16191c)}
</style>
</head>
<body>
<main class="deck">

<section class="slide">
  <div class="ph" style="left:150px;top:0;width:186px;height:189px;background:linear-gradient(100deg,#f1f5f8 0,#cfdee7 35%,#a8bcc8 70%,#7f96a4)" role="img" aria-label="Médico sorridente de bata branca"></div>
  <div class="brand" style="left:17px;top:44px;font-size:11.5px"><i style="width:16px;height:16px"></i>CLÍNICA HORIZONTE</div>
  <div class="abs" style="left:50px;top:62px;font-size:5px;color:var(--navy)">Prof. Doutor Rui Almada</div>
  <div class="abs" style="left:20px;top:79px;font-size:13px;color:var(--blue);line-height:13.5px">Click here to<br>include <b>your Title</b><br><b>Presentation</b></div>
  <div class="abs" style="left:20px;top:125px;font-size:8.5px;color:var(--sky)">Your subtitle slide goes here</div>
  <div class="abs" style="left:20px;top:139px;font-size:7.5px;color:var(--sky)">Your name here</div>
  <div class="abs" style="left:20px;top:150px;font-size:4px;color:var(--sky)">CEO &amp; Founder</div>
  <div class="abs" style="left:20px;top:160px;font-size:7px;color:var(--sky)">September 2022</div>
  <div class="abs" style="left:105px;top:180px;font-size:4.5px;letter-spacing:3px;color:var(--sky)">www.clinicahorizonte.pt</div>
</section>

<section class="slide">
  <div class="brand" style="left:14px;top:14px;font-size:7px"><i style="width:10px;height:10px"></i>CLÍNICA HORIZONTE</div>
  <div class="abs" style="left:35px;top:68px;font-size:16px;color:var(--blue);line-height:17px">Table of<br><b>content</b></div>
  <div class="abs" style="left:35px;top:118px;font-size:5px;color:var(--grey)">Centro de Congressos do Tejo</div>
  <div class="abs" style="left:35px;top:131px;font-size:5px;color:var(--grey)">Octuber 2022</div>
  <div class="abs" style="left:150px;top:54px;font-size:6.6px;color:var(--grey);line-height:12.5px">
    Click here to include title section<br>Click here to include title section<br>Click here to include title section<br>Click here to include title section<br>Click here to include title section<br>Click here to include title section<br>Click here to include title section<br>Click here to include title section
  </div>
  <div class="abs" style="left:290px;top:54px;height:100px;border-left:1px solid var(--mute)"></div>
  <div class="abs" style="left:302px;top:54px;font-size:7px;color:var(--sky);line-height:12.5px">01<br>02<br>03<br>04<br>05<br>06<br>07<br>08</div>
  <div class="footer"><span>Copyright © 2022 Clínica Horizonte | All Rights Reserved.</span><span>www.clinicahorizonte.pt | 2</span></div>
</section>

<section class="slide">
  <div class="ph" style="left:170px;top:0;width:166px;height:189px;clip-path:polygon(25% 0,100% 0,100% 100%,0 100%);background:linear-gradient(135deg,#dfe7ec,#9eb0bb 55%,#55697a)" role="img" aria-label="Médica a observar uma radiografia"></div>
  <div class="brand" style="left:11px;top:14px;font-size:7px"><i style="width:10px;height:10px"></i>CLÍNICA HORIZONTE</div>
  <div class="abs" style="left:11px;top:52px;font-size:10px;color:var(--blue)">Sobre <b>Nós</b></div>
  <ul class="bullets abs" style="left:11px;top:73px;width:150px;font-size:5.8px;color:var(--ink);line-height:7.4px">
    <li style="margin-bottom:5.5px;padding-left:20px">Despesa com a montagem da plataforma informática fica completamente do nosso lado</li>
    <li style="margin-bottom:5.5px;padding-left:20px">Não existe qualquer pagamento inicial</li>
    <li style="margin-bottom:5.5px;padding-left:20px">Não existem quaisquer custos fixos ou um mínimo de exames obrigatório</li>
    <li style="margin-bottom:5.5px;padding-left:20px">Temos simplesmente um preço por relatório</li>
    <li style="padding-left:20px">São faturados apenas os relatórios efectivados</li>
  </ul>
  <div class="abs" style="left:14px;top:182px;font-size:3.3px;color:var(--mute)">Copyright © 2022 Clínica Horizonte | All Rights Reserved.</div>
</section>

<section class="slide">
  <div class="slide-title">Our <b>Direção</b></div>
  <div class="brand small"><i></i>CLÍNICA HORIZONTE</div>
  <div class="ph photo-dark" style="left:17px;top:28px;width:94px;height:114px" role="img" aria-label="Retrato do Presidente Executivo de fato escuro"></div>
  <div class="abs" style="left:10px;top:145px;width:108px;text-align:center;font-size:5.8px;line-height:6.5px">Prof. Doutor Rui Almada<br>Presidente Executivo</div>
  <div class="abs" style="left:124px;top:29px;width:205px;font-size:3.6px;line-height:5.6px;color:var(--ink)">
    <div class="bio-head">Educação Universitária</div>
    <ul class="bullets"><li>Licenciado em Medicina pela Faculdade de Ciências Médicas, com classificação final de 18 valores.</li><li>Doutorado em Medicina, aprovado com distinção e louvor.</li></ul>
    <div class="bio-head">Educação Pós-Graduada</div>
    <ul class="bullets"><li>Internato de Imagiologia e Radiodiagnóstico em hospital universitário.</li><li>Fellowship clínico em Imagiologia Vascular num centro académico internacional.</li><li>Fellowship clínico em Imagiologia Músculo-Esquelética num serviço de radiologia osteoarticular.</li></ul>
    <div class="bio-head">Funções Actuais</div>
    <ul class="bullets"><li>CEO da Clínica Horizonte.</li><li>Membro da comissão editorial de uma revista científica de ortopedia.</li><li>Grau de Consultor em Imagiologia pelo Colégio Nacional de Radiologia.</li><li>Professor Auxiliar Convidado e Regente de Disciplina.</li><li>Investigador num centro de investigação em saúde.</li></ul>
  </div>
  <div class="footer"><span>Copyright © 2022 Clínica Horizonte | All Rights Reserved.</span><span>www.clinicahorizonte.pt | 4</span></div>
</section>

<section class="slide">
  <div class="slide-title">Meet our <b>Direção</b></div>
  <div class="brand small"><i></i>CLÍNICA HORIZONTE</div>
  <svg class="abs" style="left:0;top:0" width="336" height="189" viewBox="0 0 336 189" role="img" aria-label="Retratos da equipa de direção">
    <defs><linearGradient id="face" x1="0" y1="0" x2="0" y2="1"><stop offset="0" stop-color="#dbe9f1"/><stop offset="1" stop-color="#9fb8c7"/></linearGradient></defs>
    <g font-family="Montserrat,sans-serif" font-size="4.2" font-weight="700" fill="#fff">
      <g transform="translate(50,60)"><circle r="25" fill="url(#face)"/><path d="M-25 20h48l5 6h-53z" fill="#2a9bd1"/><text x="-22" y="25">Name Surname</text></g>
      <g transform="translate(130,60)"><circle r="25" fill="url(#face)"/><path d="M-25 20h48l5 6h-53z" fill="#2a9bd1"/><text x="-22" y="25">Name Surname</text></g>
      <g transform="translate(210,60)"><circle r="25" fill="url(#face)"/><path d="M-25 20h48l5 6h-53z" fill="#2a9bd1"/><text x="-22" y="25">Name Surname</text></g>
      <g transform="translate(288,60)"><circle r="25" fill="url(#face)"/><path d="M-25 19h48l5 6h-53z" fill="#2a9bd1"/><text x="-22" y="24">Name Surname</text></g>
      <g transform="translate(50,130)"><circle r="25" fill="url(#face)"/><path d="M-25 20h48l5 6h-53z" fill="#2a9bd1"/><text x="-22" y="25">Name Surname</text></g>
      <g transform="translate(130,130)"><circle r="25" fill="url(#face)"/><path d="M-25 20h48l5 6h-53z" fill="#2a9bd1"/><text x="-22" y="25">Name Surname</text></g>
      <g transform="translate(210,130)"><circle r="25" fill="url(#face)"/><path d="M-25 20h48l5 6h-53z" fill="#2a9bd1"/><text x="-22" y="25">Name Surname</text></g>
      <g transform="translate(288,130)"><circle r="25" fill="url(#face)"/><path d="M-25 19h48l5 6h-53z" fill="#2a9bd1"/><text x="-22" y="24">Name Surname</text></g>
    </g>
  </svg>
  <div class="footer"><span>Copyright © 2022 Clínica Horizonte | All Rights Reserved.</span><span>www.clinicahorizonte.pt | 5</span></div>
</section>

<section class="slide">
  <div class="ph" style="left:14px;top:14px;width:308px;height:88px;background:linear-gradient(90deg,#f4f8fb 0,#e2edf4 40%,#9cc0d6 70%,#5e93b4)" role="img" aria-label="Médico a tocar as mãos de um paciente"></div>
  <div class="brand" style="left:20px;top:21px;font-size:7px"><i style="width:10px;height:10px"></i>CLÍNICA HORIZONTE</div>
  <div class="abs" style="left:20px;top:45px;font-size:10.5px;color:var(--blue);line-height:12.5px">Our <b>Excellence Service</b><br>Provide All Assurance</div>
  <div class="abs" style="left:20px;top:77px;width:130px;font-size:3.4px;color:var(--blue);line-height:5px">Lorem ipsum dolor sit amet, consectetur adipiscing elit, sed do eiusmod tempor incididunt ut labore et dolore magna aliqua.</div>
  <div class="abs" style="left:14px;top:102px;width:308px;height:73px;display:grid;grid-template-columns:repeat(5,1fr)">
    <div style="background:#2b95c9"></div><div style="background:#3ea4d6"></div><div style="background:#2b95c9"></div><div style="background:#3ea4d6"></div><div style="background:#236f9b"></div>
  </div>
  <svg class="abs" style="left:14px;top:102px" width="308" height="73" viewBox="0 0 308 73" fill="none" stroke="#fff" stroke-width="1">
    <rect x="22" y="6" width="18" height="20" rx="1"/><path d="M25 10h12M25 15h4M31 15h4M25 20h4M31 20h4"/>
    <circle cx="92" cy="13" r="8"/><path d="M88 20l-3 8 7-3 7 3-3-8"/>
    <path d="M154 6l9 3v7c0 5-4 9-9 11-5-2-9-6-9-11V9z" fill="#fff"/><path d="M150 16l3 3 6-6" stroke="#2b95c9"/>
    <path d="M210 10l2 2 4-4M210 17l2 2 4-4M210 24l2 2 4-4M220 11h14M220 18h14M220 25h14"/>
    <path d="M276 13l12-6 12 6-12 6z"/><path d="M281 16v6c4 3 10 3 14 0v-6M300 13v7"/>
  </svg>
  <div class="abs" style="left:14px;top:131px;width:308px;display:grid;grid-template-columns:repeat(5,1fr);text-align:center;color:#fff">
    <div style="padding:0 4px"><div style="font-size:4.5px">Service One</div><div style="font-size:3.3px;line-height:4.5px;margin-top:5px;opacity:.85">Lorem ipsum dolor sit amet, consect adipiscing elit in lorem amet</div></div>
    <div style="padding:0 4px"><div style="font-size:4.5px">Service Two</div><div style="font-size:3.3px;line-height:4.5px;margin-top:5px;opacity:.85">Lorem ipsum dolor sit amet, consect adipiscing elit in lorem amet</div></div>
    <div style="padding:0 4px"><div style="font-size:4.5px">Service Three</div><div style="font-size:3.3px;line-height:4.5px;margin-top:5px;opacity:.85">Lorem ipsum dolor sit amet, consect adipiscing elit in lorem amet</div></div>
    <div style="padding:0 4px"><div style="font-size:4.5px">Service Four</div><div style="font-size:3.3px;line-height:4.5px;margin-top:5px;opacity:.85">Lorem ipsum dolor sit amet, consect adipiscing elit in lorem amet</div></div>
    <div style="padding:0 4px"><div style="font-size:4.5px">Service Four</div><div style="font-size:3.3px;line-height:4.5px;margin-top:5px;opacity:.85">Lorem ipsum dolor sit amet, consect adipiscing elit in lorem amet</div></div>
  </div>
  <div class="footer"><span>Copyright © 2022 Clínica Horizonte | All Rights Reserved.</span><span>www.clinicahorizonte.pt | 6</span></div>
</section>

<section class="slide">
  <div class="slide-title">Sobre <b>Nós</b></div>
  <div class="brand small"><i></i>CLÍNICA HORIZONTE</div>
  <svg class="abs" style="left:0;top:0" width="336" height="189" viewBox="0 0 336 189" font-family="Montserrat,sans-serif">
    <defs><marker id="ar" markerWidth="4" markerHeight="4" refX="3" refY="2" orient="auto"><path d="M0 0L4 2L0 4z" fill="#2a9bd1"/></marker></defs>
    <g stroke="#2a9bd1" stroke-width=".5" fill="none" marker-end="url(#ar)">
      <path d="M148 55L94 134"/><path d="M194 55L248 134"/><path d="M202 147H118"/>
    </g>
    <rect x="133" y="27" width="55" height="20" rx="2" fill="#0c4d6e"/>
    <text x="160.5" y="40" fill="#fff" font-size="6" text-anchor="middle" letter-spacing=".8">Research</text>
    <circle cx="140" cy="26" r="6" fill="#fff" stroke="#0c4d6e"/><circle cx="140" cy="26" r="3.5" fill="#1a8fc4"/>
    <rect x="58" y="136" width="55" height="20" rx="2" fill="#2a9bd1"/>
    <text x="85.5" y="149" fill="#fff" font-size="6" text-anchor="middle" letter-spacing=".8">Business</text>
    <circle cx="57" cy="135" r="6" fill="#fff" stroke="#0c4d6e"/><circle cx="57" cy="135" r="3.5" fill="#1a8fc4"/>
    <rect x="224" y="136" width="55" height="20" rx="2" fill="#5cbde6"/>
    <text x="251.5" y="149" fill="#fff" font-size="6" text-anchor="middle" letter-spacing=".8">Education</text>
    <circle cx="225" cy="135" r="6" fill="#fff" stroke="#0c4d6e"/><circle cx="225" cy="135" r="3.5" fill="#1a8fc4"/>
    <g font-size="4.8" fill="#7fc1e0" text-anchor="middle">
      <text x="82" y="80">Business opportunities</text><text x="84" y="86">point to new research</text><text x="94" y="92">avenues</text>
      <text x="175" y="67">New knowledge</text><text x="180" y="73">improves</text><text x="182" y="79">education</text>
      <text x="247" y="86">Skills are a key input in</text><text x="237" y="92">research and</text><text x="242" y="98">developments</text>
      <text x="138" y="116">New knowledge is the</text><text x="134" y="122">source of innovation</text>
    </g>
    <g font-size="4.8" fill="#556470" text-anchor="middle">
      <text x="165" y="140">Skills are a key input in innovation</text>
      <text x="165" y="153">Knowledge of new market</text><text x="165" y="159">developments is important for</text><text x="165" y="165">education</text>
    </g>
  </svg>
  <div class="footer"><span>Copyright © 2022 Clínica Horizonte | All Rights Reserved.</span><span>www.clinicahorizonte.pt | 7</span></div>
</section>

<section class="slide">
  <div class="ph" style="left:0;top:18px;width:120px;height:171px;background:linear-gradient(180deg,#f2f5f7,#e4eaee)" role="img" aria-label="Mapa de África com Angola destacada"></div>
  <div class="slide-title">IMAGIOLOGIA <b>EM ANGOLA</b></div>
  <div class="brand small"><i></i>CLÍNICA HORIZONTE</div>
  <div class="abs" style="left:0;width:336px;top:43px;text-align:center;font-size:8px;color:var(--ink);letter-spacing:.3px">CONTEXTO DE OPORTUNIDADE</div>
  <div class="ph" style="left:30px;top:75px;width:40px;height:45px;border-radius:6px;background:var(--blue)" role="img" aria-label="Silhueta de Angola"></div>
  <div class="abs" style="left:87px;top:64px;width:80px;height:31px;border-radius:3px;background:var(--navy);color:#fff;font-size:5.6px;line-height:6.5px;padding:4px 4px;box-shadow:0 1px 3px rgba(0,0,0,.3)">Carência dramática de cuidados na área da Imagiologia</div>
  <div class="abs" style="left:87px;top:108px;width:80px;height:36px;border-radius:3px;background:var(--blue);color:#fff;font-size:5.6px;line-height:6.5px;padding:5px 4px;box-shadow:0 1px 3px rgba(0,0,0,.3)">População urbana em rápido crescimento. Aumento do PIB</div>
  <svg class="abs" style="left:165px;top:78px" width="60" height="50" viewBox="0 0 60 50">
    <path d="M2 10C20 12 32 20 40 30l4-4 2 14-13-2 4-4C30 22 18 16 2 16z" fill="#0c4d6e"/>
    <path d="M2 40C18 38 30 30 38 24l-4-3 12-1-3 12-3-4C32 34 20 44 2 46z" fill="#2a9bd1"/>
    <circle cx="28" cy="25" r="4" fill="#fff" stroke="#0c4d6e" stroke-width=".6"/>
  </svg>
  <div class="abs" style="left:222px;top:84px;width:87px;height:40px;border-radius:3px;background:var(--navy);border:1px solid var(--sky);color:#fff;font-size:6.6px;line-height:7.5px;text-align:center;display:flex;align-items:center;justify-content:center;box-shadow:0 1px 3px rgba(0,0,0,.3)">Oportunidade<br>comercial relevante</div>
  <div class="footer"><span>Copyright © 2022 Clínica Horizonte | All Rights Reserved.</span><span>www.clinicahorizonte.pt | 8</span></div>
</section>

<section class="slide">
  <div class="slide-title">IMAGIOLOGIA <b>EM ANGOLA</b></div>
  <div class="brand small"><i></i>CLÍNICA HORIZONTE</div>
  <div class="abs" style="left:39px;top:45px;font-size:7.5px;color:var(--ink)">A DIFICULDADE</div>
  <div class="abs" style="left:194px;top:45px;font-size:7.5px;color:var(--ink)">A HIPÓTESE</div>
  <div class="abs" style="left:36px;top:67px;width:60px;height:35px;border-radius:3px;background:#7b7f83;color:#fff;font-size:5.6px;line-height:6.5px;text-align:center;display:flex;align-items:center;justify-content:center">Falta de Médicos<br>Radiologistas</div>
  <div class="abs" style="left:36px;top:110px;width:60px;height:35px;border-radius:3px;background:#a6aaad;color:#fff;font-size:5.6px;line-height:6.5px;text-align:center;display:flex;align-items:center;justify-content:center">Limitações na<br>qualidade</div>
  <svg class="abs" style="left:97px;top:67px" width="28" height="78" viewBox="0 0 28 78"><path d="M0 0L26 39 0 78z" fill="#dfe3e6"/></svg>
  <div class="abs" style="left:140px;top:67px;width:60px;height:35px;border-radius:3px;background:var(--blue);color:#fff;font-size:5.6px;line-height:6.5px;text-align:center;display:flex;align-items:center;justify-content:center">Expatriar<br>Profissionais<br>Portugueses</div>
  <div class="abs" style="left:140px;top:110px;width:60px;height:35px;border-radius:3px;background:var(--navy);color:#fff;font-size:5.8px;text-align:center;display:flex;align-items:center;justify-content:center">Elevado custo</div>
  <ul class="bullets abs" style="left:228px;top:69px;width:78px;font-size:5.5px;line-height:6.4px;color:var(--grey)">
    <li>Serviço de qualidade Europeia: necessários pelo menos 7 Médicos Radiologistas nas diferentes sub-especialidades</li>
    <li>Portugal e Brasil também com enorme falta de Médicos</li>
    <li>Custo elevado fixo</li>
  </ul>
  <div class="footer"><span>Copyright © 2022 Clínica Horizonte | All Rights Reserved.</span><span>www.clinicahorizonte.pt | 9</span></div>
</section>

<section class="slide">
  <div class="slide-title">Os nossos <b>Servicios</b></div>
  <div class="brand small"><i></i>CLÍNICA HORIZONTE</div>
  <div class="abs" style="left:18px;top:40px;width:303px;display:grid;grid-template-columns:repeat(4,70px);column-gap:7px;font-size:3.4px;line-height:4.4px;color:var(--ink)">
    <div>
      <div class="ph" style="position:relative;height:90px;border-radius:3px;background:linear-gradient(135deg,#f7e5e8,#e8c6cc)" role="img" aria-label="Estetoscópio em tons rosados"></div>
      <div style="font-size:5.2px;color:var(--blue);text-align:center;margin:4px 0 3px">Serviço Internacional</div>
      <div style="text-align:justify">Lorem ipsum dolor sit amet, consectetur adipiscing elit, sed do eiusmod tempor incididunt ut labore.</div>
    </div>
    <div>
      <div class="ph" style="position:relative;height:90px;border-radius:3px;background:linear-gradient(135deg,#eef2f4,#b9c6cf)" role="img" aria-label="Médica a analisar um exame"></div>
      <div style="font-size:5.2px;color:var(--blue);text-align:center;margin:4px 0 3px">Serviço de Dia e Noite</div>
      <div style="text-align:justify">Lorem ipsum dolor sit amet, consectetur adipiscing elit, sed do eiusmod tempor incididunt ut labore.</div>
    </div>
    <div>
      <div class="ph" style="position:relative;height:90px;border-radius:3px;background:linear-gradient(135deg,#e6eef3,#8ea6b6)" role="img" aria-label="Médico de óculos e bata"></div>
      <div style="font-size:5.2px;color:var(--blue);text-align:center;margin:4px 0 3px">Sub-Especialidades</div>
      <div style="text-align:justify">Lorem ipsum dolor sit amet, consectetur adipiscing elit, sed do eiusmod tempor incididunt ut labore.</div>
    </div>
    <div>
      <div class="ph" style="position:relative;height:90px;border-radius:3px;background:linear-gradient(135deg,#eef3f6,#a8bccb)" role="img" aria-label="Médicos a rever imagens de ressonância"></div>
      <div style="font-size:5.2px;color:var(--blue);text-align:center;margin:4px 0 3px">Ressonância Magnética</div>
      <div style="text-align:justify">Lorem ipsum dolor sit amet, consectetur adipiscing elit, sed do eiusmod tempor incididunt ut labore.</div>
    </div>
  </div>
  <div class="abs" style="left:18px;top:40px;width:303px;display:grid;grid-template-columns:repeat(4,70px);column-gap:7px">
    <span style="width:10px;height:9px;background:var(--sky);color:#fff;font-size:4px;text-align:center;line-height:9px">01</span>
    <span style="width:10px;height:9px;background:var(--sky);color:#fff;font-size:4px;text-align:center;line-height:9px">02</span>
    <span style="width:10px;height:9px;background:var(--sky);color:#fff;font-size:4px;text-align:center;line-height:9px">03</span>
    <span style="width:10px;height:9px;background:var(--sky);color:#fff;font-size:4px;text-align:center;line-height:9px">04</span>
  </div>
  <div class="footer"><span>Copyright © 2022 Clínica Horizonte | All Rights Reserved.</span><span>www.clinicahorizonte.pt | 9</span></div>
</section>

<section class="slide">
  <div class="slide-title"><b>Sub-Especialidades</b></div>
  <div class="brand small"><i></i>CLÍNICA HORIZONTE</div>
  <div class="ph" style="left:10px;top:30px;width:120px;height:131px;background:linear-gradient(90deg,#c7d4dc,#eef3f6 60%,#d3dde3)" role="img" aria-label="Médico sorridente num corredor hospitalar"></div>
  <div class="abs" style="left:146px;top:36px;width:172px;font-size:4.2px;line-height:5px;color:var(--grey)">
    <p>Todos os nossos exames de Ressonância Magnética são interpretados por sub-especialistas de elite nas diferentes áreas.</p>
    <p style="margin-top:2px">Os nossos clientes têm assim a possibilidade única de ter ao seu serviço, na sua clínica, os melhores médicos, contribuindo para o incremento quantitativo e qualitativo da Instituição.</p>
    <p style="margin-top:2px">Temos como principais áreas de diferenciação dos nossos profissionais:</p>
    <ul class="bullets" style="margin:2px 0 0 2px;line-height:8px">
      <li>Músculo-Esquelético</li><li>Medicina desportiva</li><li>Neurorradiologia</li><li>Abdómen</li><li>Pélvis</li><li>Sistema cardiovascular</li><li>Mama</li>
    </ul>
    <p style="margin-top:2px">Poderá optar por serviços de apenas uma ou algumas das sub-especialidades, para preencher necessidades pontuais ou para afirmar no mercado particular diferenciação numa determinada área.</p>
  </div>
  <div class="footer"><span>Copyright © 2022 Clínica Horizonte | All Rights Reserved.</span><span>www.clinicahorizonte.pt | 10</span></div>
</section>

<section class="slide">
  <div class="slide-title">Our Data and comments <b>in One Slide</b></div>
  <div class="brand small"><i></i>CLÍNICA HORIZONTE</div>
  <svg class="abs" style="left:0;top:0" width="336" height="189" viewBox="0 0 336 189" font-family="Montserrat,sans-serif">
    <text x="168" y="37" font-size="5" fill="#8a949b" text-anchor="middle">Chart Title</text>
    <g stroke="#e5e9ec" stroke-width=".4"><path d="M20 43h300M20 53.5h300M20 64h300M20 74.5h300M20 85h300M20 95.5h300M20 106h300"/></g>
    <g font-size="3" fill="#9aa3a9" text-anchor="end"><text x="16" y="44">6</text><text x="16" y="54.5">5</text><text x="16" y="65">4</text><text x="16" y="75.5">3</text><text x="16" y="86">2</text><text x="16" y="96.5">1</text><text x="16" y="107">0</text></g>
    <g>
      <rect x="33" y="61" width="13" height="45" fill="#1175a8"/><rect x="48" y="80.8" width="13" height="25.2" fill="#3aa8da"/><rect x="63" y="85" width="13" height="21" fill="#0c4d6e"/>
      <rect x="108" y="59.8" width="13" height="46.2" fill="#3aa8da"/><rect x="93" y="79.8" width="13" height="26.2" fill="#1175a8"/><rect x="123" y="85" width="13" height="21" fill="#0c4d6e"/>
      <rect x="183" y="69.3" width="13" height="36.7" fill="#1175a8"/><rect x="198" y="87.1" width="13" height="18.9" fill="#3aa8da"/><rect x="213" y="74.5" width="13" height="31.5" fill="#0c4d6e"/>
      <rect x="258" y="59.3" width="13" height="46.7" fill="#1175a8"/><rect x="273" y="76.6" width="13" height="29.4" fill="#3aa8da"/><rect x="288" y="53.5" width="13" height="52.5" fill="#0c4d6e"/>
    </g>
    <g font-size="3" fill="#9aa3a9" text-anchor="middle"><text x="55" y="112">Category 1</text><text x="115" y="112">Category 2</text><text x="205" y="112">Category 3</text><text x="280" y="112">Category 4</text></g>
    <g font-size="3" fill="#9aa3a9"><rect x="136" y="116" width="2" height="2" fill="#1175a8"/><text x="139" y="118">Series 1</text><rect x="153" y="116" width="2" height="2" fill="#3aa8da"/><text x="156" y="118">Series 2</text><rect x="170" y="116" width="2" height="2" fill="#0c4d6e"/><text x="173" y="118">Series 3</text></g>
  </svg>
  <ul class="bullets abs" style="left:18px;top:125px;width:302px;font-size:3.3px;line-height:4px;color:var(--ink);text-align:justify">
    <li style="margin-bottom:3px">Lorem ipsum dolor sit amet, consectetur adipiscing elit, sed do eiusmod tempor incididunt ut labore et dolore magna aliqua. Ut enim ad minim veniam, quis nostrud exercitation ullamco laboris nisi ut aliquip ex ea commodo consequat duis aute irure.</li>
    <li style="margin-bottom:3px">Duis aute irure dolor in reprehenderit in voluptate velit esse cillum dolore eu fugiat nulla pariatur, excepteur sint occaecat cupidatat non proident.</li>
    <li>Sed ut perspiciatis unde omnis iste natus error sit voluptatem accusantium doloremque laudantium, totam rem aperiam, eaque ipsa quae ab illo inventore veritatis et quasi architecto.</li>
  </ul>
  <div class="footer"><span>Copyright © 2022 Clínica Horizonte | All Rights Reserved.</span><span>www.clinicahorizonte.pt | 11</span></div>
</section>

<section class="slide">
  <div class="slide-title">Your title <b>Data Slide</b></div>
  <div class="brand small"><i></i>CLÍNICA HORIZONTE</div>
  <svg class="abs" style="left:0;top:0" width="336" height="189" viewBox="0 0 336 189" font-family="Montserrat,sans-serif">
    <text x="100" y="42" font-size="5.5" fill="#8a949b" text-anchor="middle">Chart Title</text>
    <g stroke="#e1e5e8" stroke-width=".4" fill="none"><path d="M25 136h120l30-15M25 55v81M25 55l30-15"/></g>
    <g font-size="3" fill="#9aa3a9" text-anchor="end"><text x="22" y="131">0.5</text><text x="22" y="115">1.5</text><text x="22" y="99">2.5</text><text x="22" y="83">3.5</text><text x="22" y="67">4.5</text></g>
    <g>
      <rect x="45" y="96" width="10" height="32" fill="#1175a8"/><rect x="55" y="94" width="4" height="32" fill="#0c4d6e"/>
      <rect x="73" y="104" width="10" height="24" fill="#1175a8"/><rect x="83" y="102" width="4" height="24" fill="#0c4d6e"/>
      <rect x="101" y="79" width="10" height="49" fill="#1175a8"/><rect x="111" y="77" width="4" height="49" fill="#0c4d6e"/>
      <rect x="129" y="62" width="10" height="66" fill="#1175a8"/><rect x="139" y="60" width="4" height="66" fill="#0c4d6e"/>
      <rect x="40" y="104" width="10" height="28" fill="#3aa8da"/><rect x="68" y="100" width="10" height="32" fill="#3aa8da"/>
      <rect x="96" y="106" width="10" height="26" fill="#3aa8da"/><rect x="124" y="96" width="10" height="36" fill="#3aa8da"/>
      <rect x="33" y="100" width="11" height="36" fill="#a2a7ab"/><rect x="44" y="98" width="3" height="36" fill="#7b8084"/>
      <rect x="61" y="112" width="11" height="24" fill="#a2a7ab"/><rect x="72" y="110" width="3" height="24" fill="#7b8084"/>
      <rect x="89" y="104" width="11" height="32" fill="#a2a7ab"/><rect x="100" y="102" width="3" height="32" fill="#7b8084"/>
      <rect x="117" y="100" width="11" height="36" fill="#a2a7ab"/><rect x="128" y="98" width="3" height="36" fill="#7b8084"/>
    </g>
    <g font-size="3" fill="#9aa3a9"><text x="30" y="142">Category 1</text><text x="58" y="142">Category 2</text><text x="86" y="142">Category 3</text><text x="114" y="142">Category 4</text><text x="160" y="117">Series 3</text><text x="153" y="124">Series 2</text><text x="146" y="131">Series 1</text></g>
    <g font-size="3" fill="#9aa3a9"><rect x="72" y="151" width="2" height="2" fill="#1175a8"/><text x="75" y="153">Series 1</text><rect x="89" y="151" width="2" height="2" fill="#3aa8da"/><text x="92" y="153">Series 2</text><rect x="106" y="151" width="2" height="2" fill="#a2a7ab"/><text x="109" y="153">Series 3</text></g>
  </svg>
  <div class="abs" style="left:200px;top:41px;font-size:5.5px;color:var(--blue)">Your subtitle <b>data slide goes here</b></div>
  <ul class="bullets abs" style="left:196px;top:55px;width:122px;font-size:3.4px;line-height:4.1px;color:var(--ink);text-align:justify">
    <li style="margin-bottom:4px">Lorem ipsum dolor sit amet, consectetur adipiscing elit, sed do eiusmod tempor incididunt ut labore et dolore magna aliqua. Ut enim ad minim veniam, quis nostrud exercitation ullamco laboris nisi ut aliquip ex ea commodo consequat.</li>
    <li style="margin-bottom:4px">Duis aute irure dolor in reprehenderit in voluptate velit esse cillum dolore eu fugiat nulla pariatur, excepteur sint occaecat cupidatat.</li>
    <li>Sed ut perspiciatis unde omnis iste natus error sit voluptatem accusantium doloremque laudantium, totam rem aperiam, eaque ipsa quae ab illo inventore veritatis et quasi architecto beatae vitae dicta sunt explicabo.</li>
  </ul>
  <div class="footer"><span>Copyright © 2022 Clínica Horizonte | All Rights Reserved.</span><span>www.clinicahorizonte.pt | 12</span></div>
</section>

<section class="slide">
  <div class="ph" style="inset:0;background:linear-gradient(180deg,#56b3df,#2a9bd1 55%,#2e9ed3)" role="img" aria-label="Equipa de profissionais de saúde sorridentes em tons de azul"></div>
  <div class="abs" style="left:0;width:336px;top:82px;text-align:center;color:#fff">
    <div style="font-size:21px;font-weight:800;line-height:24px">Muito obrigado</div>
    <div style="font-size:21px;font-weight:300;line-height:26px">pela sua atenção</div>
  </div>
</section>

<section class="slide">
  <div class="ph" style="left:160px;top:0;width:176px;height:189px;clip-path:polygon(28% 0,100% 0,100% 100%,0 100%);background:linear-gradient(90deg,#f3f6f8,#d5dfe5 35%,#aebfc9)" role="img" aria-label="Equipa médica sorridente"></div>
  <div class="brand" style="left:20px;top:16px;font-size:8px"><i style="width:12px;height:12px"></i>CLÍNICA HORIZONTE</div>
  <div class="abs" style="left:21px;top:37px;font-size:11px;color:var(--navy)"><b>CONTACT</b> US</div>
  <div class="abs" style="left:17px;top:60px;width:135px;font-size:3.4px;line-height:4.3px;color:var(--grey)">Thank you for your cooperation and support extended to us during the course of our services. If there are any questions or comments, please feel free to contact us via any method listed below.</div>
  <svg class="abs" style="left:16px;top:82px" width="16" height="88" viewBox="0 0 16 88">
    <g fill="#2a9bd1"><rect width="16" height="16"/><rect y="24" width="16" height="16"/><rect y="48" width="16" height="16"/><rect y="72" width="16" height="16"/></g>
    <g fill="#fff"><path d="M8 3a4 4 0 0 1 4 4c0 3-4 6-4 6S4 10 4 7a4 4 0 0 1 4-4z"/><circle cx="8" cy="7" r="1.5" fill="#2a9bd1"/>
    <path d="M4 29c0-1 1-2 4-2s4 1 4 2l-1 1H5zM5 31h6l1 5H4z"/></g>
    <g fill="none" stroke="#fff" stroke-width=".8"><rect x="3.5" y="52.5" width="9" height="7"/><path d="M3.5 52.5l4.5 4 4.5-4"/><circle cx="8" cy="80" r="4.5"/><path d="M3.5 80h9M8 75.5c-2 2.5-2 6.5 0 9M8 75.5c2 2.5 2 6.5 0 9"/></g>
  </svg>
  <div class="abs" style="left:49px;top:83px;font-size:3.6px;line-height:4.4px;color:var(--ink)">Edifício Atlântico<br>Rua das Flores 12, 2º<br>1200-195 Lisboa, Portugal</div>
  <div class="abs" style="left:49px;top:110px;font-size:3.6px;line-height:4.4px;color:var(--ink)">+351 910 000 111<br>+351 920 000 222</div>
  <div class="abs" style="left:49px;top:136px;font-size:3.6px;color:var(--ink)">info@clinicahorizonte.pt</div>
  <div class="abs" style="left:49px;top:158px;font-size:3.6px;color:var(--ink)">www.clinicahorizonte.pt</div>
</section>

</main>
</body>
</html>
```